Coffee Package Design

We need a new package design for a coffee company. Need to be a mix between modern and classic design combined together. We are open to different ideas.
We changing our product name from Café Verlona to Café Rostelli. The picture upload
shows what the product looks like. We want something completely different. The name of the company should go on the back of the package.
Updates

Hello Everyone,

Please read description, we are going with a new name and design for the product.

Café Rostelli. Café Verlona is what we are replacing with Café Rostelli, we are looking for new

look and design, please submit new designs.

There is a change in the description. Please take out Premium coffee blend and replace with Italian Roast.                                    

Industry/Entity Type

Cafe

Requirements
Must have
• You can use up to 6 colors.
Please put these items on design: Café Rostelli (this is the product name), Regular Premium Blend Coffee, 100% Arabica,
Dumbrell & Sons (name of the company), Tyler, TX on the back of the package

The file uploaded is an example of one of our products and how the package film
is sized.

```html
<!DOCTYPE html>
<html lang="en">
<head>
<meta charset="utf-8">
<title>Café Rostelli – Italian Roast Package</title>
<link rel="stylesheet" href="https://fonts.googleapis.com/css2?family=Playfair+Display:wght@500;600&family=Great+Vibes&display=swap">
<style>
  :root {
    --page-bg: #ffffff;
    --bag-red: #8e1c1f;
    --bag-red-deep: #6f1416;
    --gold: #d8b061;
    --gold-light: #f0d9a0;
    --gold-dark: #b8862f;
  }
  * { margin: 0; padding: 0; box-sizing: border-box; }
  html, body {
    width: 1200px;
    height: 946px;
    overflow: hidden;
    background: var(--page-bg);
  }
  .canvas {
    position: relative;
    width: 1200px;
    height: 946px;
  }
  .package-front {
    position: absolute;
    left: 235px;
    top: 0;
    width: 725px;
    height: 946px;
    background: linear-gradient(180deg, var(--bag-red) 0%, var(--bag-red-deep) 55%, var(--bag-red) 100%);
  }
  .package-frame {
    position: absolute;
    inset: 0;
  }
  .brand-square {
    position: absolute;
    left: 212px;
    top: 135px;
    width: 313px;
    height: 245px;
    background: linear-gradient(135deg, var(--gold-dark) 0%, var(--gold-light) 50%, var(--gold-dark) 100%);
  }
  .brand-name {
    position: absolute;
    left: 0;
    width: 100%;
    top: 424px;
    text-align: center;
    font-family: "Playfair Display", Georgia, serif;
    font-weight: 600;
    font-size: 68px;
    letter-spacing: 3px;
    text-transform: uppercase;
    color: var(--gold);
    line-height: 1;
  }
  .rule {
    position: absolute;
    height: 3px;
    background: var(--gold);
  }
  .rule--top { left: 80px; width: 565px; top: 406px; height: 2px; }
  .rule--mid { left: 75px; width: 575px; top: 540px; }
  .rule--low { left: 190px; width: 340px; top: 622px; height: 2px; }
  .roast-name {
    position: absolute;
    left: 0;
    width: 100%;
    top: 548px;
    text-align: center;
    font-family: "Great Vibes", cursive;
    font-size: 62px;
    color: var(--gold);
    line-height: 1.1;
  }
  .bean-type {
    position: absolute;
    left: 0;
    width: 100%;
    top: 634px;
    text-align: center;
    font-family: "Playfair Display", Georgia, serif;
    font-weight: 500;
    font-size: 30px;
    letter-spacing: 1px;
    color: var(--gold);
  }
  .ornament-band {
    position: absolute;
    left: 40px;
    right: 40px;
    top: 690px;
    bottom: 0;
    background:
      radial-gradient(ellipse 30% 40% at 20% 45%, rgba(216,176,97,0.28), rgba(216,176,97,0) 70%),
      radial-gradient(ellipse 30% 40% at 50% 70%, rgba(216,176,97,0.24), rgba(216,176,97,0) 70%),
      radial-gradient(ellipse 30% 40% at 80% 40%, rgba(216,176,97,0.28), rgba(216,176,97,0) 70%),
      linear-gradient(180deg, rgba(111,20,22,0) 0%, rgba(111,20,22,0.5) 100%);
  }
</style>
</head>
<body>
<main class="canvas">
  <section class="package-front">
    <svg class="package-frame" width="725" height="946" viewBox="0 0 725 946" aria-hidden="true">
      <line x1="22" y1="0" x2="22" y2="946" stroke="#d8b061" stroke-width="2"/>
      <line x1="703" y1="0" x2="703" y2="946" stroke="#d8b061" stroke-width="2"/>
      <g class="stars" fill="#d8b061">
        <path transform="translate(87 392)" d="M0,-9 L2.6,-3 L9,-2.8 L4,1.4 L5.6,8 L0,4.3 L-5.6,8 L-4,1.4 L-9,-2.8 L-2.6,-3 Z"/>
        <path transform="translate(123 392)" d="M0,-9 L2.6,-3 L9,-2.8 L4,1.4 L5.6,8 L0,4.3 L-5.6,8 L-4,1.4 L-9,-2.8 L-2.6,-3 Z"/>
        <path transform="translate(167 388)" d="M0,-9 L2.6,-3 L9,-2.8 L4,1.4 L5.6,8 L0,4.3 L-5.6,8 L-4,1.4 L-9,-2.8 L-2.6,-3 Z"/>
        <path transform="translate(562 384)" d="M0,-9 L2.6,-3 L9,-2.8 L4,1.4 L5.6,8 L0,4.3 L-5.6,8 L-4,1.4 L-9,-2.8 L-2.6,-3 Z"/>
        <path transform="translate(603 388)" d="M0,-9 L2.6,-3 L9,-2.8 L4,1.4 L5.6,8 L0,4.3 L-5.6,8 L-4,1.4 L-9,-2.8 L-2.6,-3 Z"/>
        <path transform="translate(638 392)" d="M0,-9 L2.6,-3 L9,-2.8 L4,1.4 L5.6,8 L0,4.3 L-5.6,8 L-4,1.4 L-9,-2.8 L-2.6,-3 Z"/>
      </g>
      <g class="ribbon-tails" fill="none" stroke="#d8b061" stroke-width="2">
        <path d="M95,560 L135,560 L122,578 Z"/>
        <path d="M630,560 L590,560 L603,578 Z"/>
      </g>
    </svg>
    <div class="brand-square"></div>
    <div class="rule rule--top"></div>
    <h1 class="brand-name">Café Rostelli</h1>
    <div class="rule rule--mid"></div>
    <p class="roast-name">Italian Roast</p>
    <div class="rule rule--low"></div>
    <p class="bean-type">100% Arabica</p>
    <div class="ornament-band" role="img" aria-label="Gold swirl ornament pattern across the lower part of the package"></div>
  </section>
</main>
</body>
</html>
```